Kerris Odlen Letter Head

log and letter head

would like a modern feminine approch, please see attached the back of my business card

Kerris Odlen Consulting

ABN 81 540 263 918

Address19a Brood Street Larkfield Bay 5082 Eastmoor Coast

Business

```html
<!DOCTYPE html>
<html lang="en">
<head>
<meta charset="utf-8">
<title>Kerris Odlen Consulting – Letterhead</title>
<link rel="stylesheet" href="https://fonts.googleapis.com/css2?family=EB+Garamond:wght@400;600&family=Barlow:wght@400&display=swap">
<style>
  :root {
    --brand-red: #e0242c;
    --ink: #1c1c1c;
    --paper: #ffffff;
    --signature-tone: #e4e4e4;
  }
  * { margin: 0; padding: 0; box-sizing: border-box; }
  html, body {
    width: 848px;
    height: 1200px;
    overflow: hidden;
    background: var(--paper);
  }
  .letterhead {
    position: relative;
    width: 848px;
    height: 1200px;
    background: var(--paper);
    color: var(--ink);
    font-family: "EB Garamond", Georgia, serif;
  }
  .brand {
    position: absolute;
    top: 62px;
    left: 0;
    width: 100%;
    text-align: center;
    color: var(--brand-red);
    font-family: "EB Garamond", Georgia, serif;
    font-weight: 400;
  }
  .brand-name {
    display: block;
    font-size: 76px;
    line-height: 92px;
    letter-spacing: 1px;
  }
  .brand-descriptor {
    display: block;
    margin-top: 12px;
    font-size: 22px;
    line-height: 26px;
    letter-spacing: 30px;
    padding-left: 30px;
  }
  .letter-title {
    position: absolute;
    top: 298px;
    left: 154px;
    font-size: 17.5px;
    font-weight: 600;
    letter-spacing: 0.3px;
    text-transform: uppercase;
  }
  .letter-body {
    position: absolute;
    left: 154px;
    width: 610px;
    font-size: 17px;
    line-height: 23px;
    white-space: nowrap;
  }
  .letter-body.first { top: 346px; }
  .letter-body.second { top: 523px; }
  .letter-body.third { top: 722px; }
  .signature {
    position: absolute;
    top: 892px;
    left: 157px;
    width: 186px;
    height: 148px;
    background: var(--signature-tone);
    border-radius: 4px;
  }
  .contact {
    position: absolute;
    left: 0;
    width: 100%;
    text-align: center;
    color: var(--brand-red);
    font-family: "Barlow", Arial, sans-serif;
    font-size: 16.5px;
    line-height: 20px;
  }
  .contact.address { top: 1076px; }
  .contact.abn { top: 1102px; }
</style>
</head>
<body>
<main class="letterhead">
  <header class="brand">
    <span class="brand-name">Kerris Odlen</span>
    <span class="brand-descriptor">CONSULTING</span>
  </header>

  <h1 class="letter-title">Letterhead design for Kerris Odlen</h1>

  <p class="letter-body first">
    Nonsenist ulluptate peritasit as quam, essin este nem. Illorro con nis ea natiam<br>
    facea nossintus. Equi accae mo et occus cum iumqui aliquamet, si dolorrumqui<br>
    dolupicil ipsum quatusdae autaspe digenem et, offic to te et aut ipsus milit, il is<br>
    dolorum faci diatem res unt omnis aliquo minctis unturit volorro dolut volori-<br>
    busam intiore volupta tissimped es vollandi odite pos delest, con nos destius ducid<br>
    quis et quas aboratenit omnis in nempore volupta imporer untias rem inctota<br>
    turiandae.
  </p>

  <p class="letter-body second">
    Inis de por rem quatemporunt fugia quam faceatios sinciuscit aboria cuptur sus<br>
    aliaestrum reperum dent est atur amusa veligent volorecta cus quibus ditatis<br>
    exeruntur, eseri assitatenest quam rest volorio resequam eos conestiae endae vide<br>
    volores sumquae cabori bea qui sero expedic iaectaquam quissit aestiundit officiis<br>
    pro volorum abor magnisci denditi volorro beariostiste escia corias dolupta com-<br>
    nit omnim eumquia tendelesciam labor ra dolluptiundi ut lantorehent evel eum<br>
    rem qui am nonsedi ationsectia corum harum repudam faccull anderum fugitas<br>
    volupitas.
  </p>

  <p class="letter-body third">
    Nimostia evellendia aut aut etum que peri ate paruptur atur autem quo mi, ip-<br>
    suntus nos ipsa dit everio et ut as rem fuga. Mus et, sum sequoditium sum utendi-<br>
    aspid millam, aut volupta tincid ut ut quo ducim fugitat estinum delest harumque<br>
    nonsequibus volut eatempore, cuptam harion pra eatum qui nos possit res aut<br>
    volorersped que nos minient rae cum re de officil iquunti.
  </p>

  <div class="signature" role="img" aria-label="Handwritten signature of the sender"></div>

  <footer>
    <p class="contact address">27c Tallow Lane Larkfield Bay 5082 Eastmoor Coast</p>
    <p class="contact abn">ABN 81 540 263 918</p>
  </footer>
</main>
</body>
</html>
```